Keystone Networks, it support and management

We run an IT business, so techy style would work well. We need a re-design, now that we’ve moved and phone numbers have changed.

On the back of the card I like having something that helps with taking notes, like a grid or lines

The attachment is the current business card I am using.

We specialize in helping out in all kinds of support, including laptops, desktops, servers, and providing software solutions, like deskpro 480, backups and ransomware prevention

Target Market(s)

Other small business owners, specifically smaller than 50 employees

Industry/Entity Type

SMB, but no specific niche

Contact Information for Business Card

I’d like the logo, name, my title/rolw, my contact details

Colors
0094D4
00A9DD
6FCCEA
C7EBF8
E9F6FB

Requirements
Must have
• The ability to take notes on the back of the card
Nice to have
• A new slogan or fun little quip, but not necessary
Should not have
• Street address of any kind.

```html
<!DOCTYPE html>
<html lang="en">
<head>
<meta charset="utf-8">
<title>Keystone Networks – Business Card</title>
<link rel="stylesheet" href="https://fonts.googleapis.com/css2?family=Montserrat:wght@600;700&family=Lato:wght@400;700&display=swap">
<style>
  :root {
    --bg: #e6e7ea;
    --card: #ffffff;
    --ink: #111111;
    --text: #2a2a2a;
    --blue: #4285f0;
    --grid: #b9b9b9;
  }
  * { box-sizing: border-box; margin: 0; padding: 0; }
  html, body { width: 1200px; height: 875px; overflow: hidden; }
  body {
    background: var(--bg);
    display: flex;
    align-items: center;
    justify-content: center;
    gap: 30px;
    font-family: "Lato", sans-serif;
  }
  .card {
    position: relative;
    width: 560px;
    height: 320px;
    background: var(--card);
    border-radius: 22px;
    overflow: hidden;
    box-shadow: 0 10px 30px rgba(0,0,0,.18);
  }

  /* Back: note grid */
  .card--back {
    background-color: var(--card);
    background-image:
      linear-gradient(to right, var(--grid) 1px, transparent 1px),
      linear-gradient(to bottom, var(--grid) 1px, transparent 1px);
    background-size: 40px 40px;
    background-position: 12px 10px;
  }
  .back-brand {
    position: absolute;
    top: 34px;
    right: 30px;
    background: var(--card);
    padding: 6px 10px;
    font-family: "Montserrat", sans-serif;
    font-weight: 700;
    font-size: 17px;
    white-space: nowrap;
    color: var(--blue);
  }
  .slogan {
    position: absolute;
    left: 30px;
    bottom: 28px;
    background: var(--card);
    padding: 4px 8px;
    font-family: "Montserrat", sans-serif;
    font-weight: 600;
    font-size: 17px;
    letter-spacing: 1px;
    white-space: nowrap;
    color: var(--ink);
  }
  .slogan__accent { color: var(--blue); }

  /* Front */
  .front-main {
    position: absolute;
    inset: 0 0 60px 0;
    display: flex;
    align-items: center;
    padding: 0 24px 0 32px;
  }
  .brand {
    display: flex;
    align-items: center;
    gap: 12px;
    width: 205px;
    flex: none;
  }
  .brand__dot {
    width: 24px; height: 24px;
    border-radius: 50%;
    background: var(--ink);
    flex: none;
  }
  .brand__name {
    font-family: "Montserrat", sans-serif;
    font-weight: 700;
    font-size: 23px;
    line-height: 1.15;
    color: var(--blue);
  }
  .divider {
    width: 2px;
    height: 120px;
    background: var(--ink);
    margin: 0 22px 0 8px;
    flex: none;
  }
  .person { min-width: 0; }
  .person__name {
    font-family: "Montserrat", sans-serif;
    font-weight: 700;
    font-size: 21px;
    white-space: nowrap;
    color: var(--ink);
    letter-spacing: .3px;
  }
  .person__role {
    font-size: 16px;
    color: var(--blue);
    margin: 2px 0 12px;
  }
  .contact { list-style: none; }
  .contact li {
    display: flex;
    align-items: center;
    gap: 8px;
    font-size: 14px;
    white-space: nowrap;
    color: var(--text);
    margin-bottom: 5px;
  }
  .contact svg { width: 13px; height: 13px; fill: var(--blue); flex: none; }
  .band-rule {
    position: absolute;
    left: 0; right: 0; bottom: 60px;
    height: 3px;
    background: var(--ink);
  }
  .band {
    position: absolute;
    left: 0; right: 0; bottom: 0;
    height: 54px;
    background: var(--blue);
    display: flex;
    align-items: center;
    justify-content: center;
    font-family: "Montserrat", sans-serif;
    font-weight: 600;
    font-size: 17px;
    letter-spacing: 2px;
    color: #fff;
  }
</style>
</head>
<body>
  <section class="card card--back" aria-label="Card back with note grid">
    <div class="back-brand">Keystone Networks</div>
    <div class="slogan">KEEP <span class="slogan__accent">IT RUNNING</span></div>
  </section>

  <section class="card card--front" aria-label="Card front">
    <div class="front-main">
      <div class="brand">
        <span class="brand__dot"></span>
        <span class="brand__name">Keystone Networks Inc</span>
      </div>
      <div class="divider"></div>
      <div class="person">
        <div class="person__name">DANA WHITFIELD</div>
        <div class="person__role">President</div>
        <ul class="contact">
          <li>
            <svg viewBox="0 0 16 16" aria-hidden="true"><path d="M3.5 1l2.5 3-1.5 1.8a9 9 0 0 0 5.7 5.7L12 10l3 2.5-1.6 2.4C7.6 15 1 8.4 1.1 2.6z"/></svg>
            555.014.2873x317
          </li>
          <li>
            <svg viewBox="0 0 16 16" aria-hidden="true"><path d="M4 1h8v14H4zM5.5 2.5v9h5v-9zM7 12.5h2v1H7z" fill-rule="evenodd"/></svg>
            555.019.4410
          </li>
          <li>
            <svg viewBox="0 0 16 16" aria-hidden="true"><path d="M1 3h14v10H1zM2 4l6 5 6-5z" fill-rule="evenodd"/></svg>
            dana@keystonenw.com
          </li>
        </ul>
      </div>
    </div>
    <div class="band-rule"></div>
    <div class="band">WWW.KEYSTONENW.COM</div>
  </section>
</body>
</html>
```